New Creative Busines Card

Hi Lead Designer,

How are you going?

I was hoping you can help me design the perfect business card for my new business. I have listed below some background information about the business and the concept to help with your design. I'm open to any form of creative ideas, but would like to have two types of colour schemes one dark color and one light.

I would like to have a dark set of design and a light (One design with one in black or dark background and one with light background to compare the contrast since the business card will be double sided one) I imagine this will be pretty easy to change the background of the design. Would prefer one side to have all the details and the other will just have a amazing logo (K7) to give it the finishing touch.

Feel free to email me if you have any questions.

Business Structure and design concepts:

Name of the business: K7 Advisory
Business: Dating agency and event management (Date night etc)
Concept: The main focus will be the K7 ( As some sort of a heart shape like logo) be creative
Details to include in the card will be general details like Name, Title: , Email, mobile, website (Contact details will be given later).

The rest of the idea is up to you, feel free to go crazy with your creative ideas.

Thank you for your help in advance, may the best candidate win~!

Target Market(s)

Target market will be Professional, Elegant, young and ambitious people.

Industry/Entity Type

Business

Requirements
Must have
• Focus on the K7 (as some sort of a heart shape logo). Since this is a double sides design would prefer on one side to focus on the just the K7 logo and the other side with a smaller version of the logo (with it or without) and all the details such as Name, Title, Mobile, Email, Website. Please have the design in landscape format.Not fuss with the Font as long as it is easy to read.
Nice to have
• Different Contrast in colours (keep it simple) one side dark colour scheme and one side light. Prefer to have 3-4 colours (not overwhelm with too many colours) to keep it simple and elegant.
Should not have
• Too colours, main focus is should be the K7 logo not the colours

```html
<!DOCTYPE html>
<html lang="en">
<head>
<meta charset="utf-8">
<title>K7 Advisory – Business Card</title>
<link href="https://fonts.googleapis.com/css2?family=Quicksand:wght@400;500;600&display=swap" rel="stylesheet">
<style>
  :root {
    --page: #ffffff;
    --wood-light: #7a4a2a;
    --wood-mid: #5a341d;
    --wood-dark: #2e1a0f;
    --band: rgba(18, 12, 9, 0.86);
    --band-soft: rgba(22, 15, 11, 0.8);
    --panel: #dcdcdc;
    --brand: #6b2a35;
    --ink-light: #f4f1ee;
  }
  * { margin: 0; padding: 0; box-sizing: border-box; }
  html, body {
    width: 875px;
    height: 1200px;
    overflow: hidden;
    background: var(--page);
    font-family: "Quicksand", sans-serif;
  }
  .sheet {
    position: relative;
    width: 875px;
    height: 1200px;
  }
  .card {
    position: absolute;
    left: 0;
    width: 875px;
    height: 458px;
    overflow: hidden;
  }
  .card--front { top: 127px; }
  .card--back { top: 595px; }

  .card__texture {
    position: absolute;
    inset: 0;
    background:
      radial-gradient(ellipse at 50% 45%, var(--wood-light) 0%, var(--wood-mid) 45%, var(--wood-dark) 100%);
  }
  .card--back .card__texture {
    background:
      linear-gradient(180deg, var(--wood-dark) 0%, var(--wood-light) 14%, var(--wood-mid) 40%, var(--wood-mid) 70%, var(--wood-light) 86%, var(--wood-dark) 100%);
  }

  .band {
    position: absolute;
    left: 0;
    width: 100%;
    background: var(--band);
  }
  .card--front .band { top: 155px; height: 148px; }
  .card--back .band { top: 81px; height: 272px; background: var(--band-soft); }

  .logo-panel {
    position: absolute;
    left: 303px;
    top: 105px;
    width: 273px;
    height: 234px;
    background: var(--panel);
    box-shadow: 0 0 18px rgba(0, 0, 0, 0.55);
    display: flex;
    align-items: center;
    justify-content: center;
  }
  .logo-panel__name {
    font-family: "Quicksand", sans-serif;
    font-weight: 600;
    font-size: 40px;
    color: var(--brand);
    letter-spacing: 0.5px;
  }

  .details {
    position: absolute;
    left: 14px;
    top: 96px;
    color: var(--ink-light);
  }
  .details__name {
    font-weight: 600;
    font-size: 42px;
    line-height: 1;
    padding-left: 10px;
    color: var(--ink-light);
  }
  .details__tagline {
    margin-top: 8px;
    font-weight: 400;
    font-size: 22px;
  }
  .contact {
    list-style: none;
    margin-top: 44px;
    padding-left: 10px;
  }
  .contact__item {
    font-size: 22px;
    line-height: 35px;
    font-weight: 400;
  }
  .contact__label { font-weight: 600; }
</style>
</head>
<body>
<main class="sheet">
  <section class="card card--front" aria-label="Card front">
    <div class="card__texture" role="img" aria-label="Dark wood plank background"></div>
    <div class="band"></div>
    <div class="logo-panel">
      <span class="logo-panel__name">K7 Advisory</span>
    </div>
  </section>

  <section class="card card--back" aria-label="Card back">
    <div class="card__texture" role="img" aria-label="Dark wood plank background"></div>
    <div class="band"></div>
    <div class="details">
      <h1 class="details__name">K7 Advisory</h1>
      <p class="details__tagline">Dating Agencies and Dating Managment</p>
      <ul class="contact">
        <li class="contact__item"><span class="contact__label">E-Mail</span> : mail@k7advisory.com</li>
        <li class="contact__item"><span class="contact__label">Mobile</span> : 000-00-0000</li>
        <li class="contact__item"><span class="contact__label">Website</span> : www.k7advisoryagency.com</li>
      </ul>
    </div>
  </section>
</main>
</body>
</html>
```